Brindlecove Flood Restoration needing website

Hi Team

We are looking for a 4 or 5 page website containing
1: Home
2: Services
3: Gallery
4: Equipment Hire
5 Contact Us

Would want the front page to be a big call to action. Someones house has just flooded...they're highly stressed and we just want to let them know straight away that we can assist them

Some call to action would be great.

"Wet Carpets??"

"Washing machine just overflowed??"

"Burst pipe?"

"We're here to help!!"

Would be wanting a scrolling banner type homepage with images of flooded houses, heavy rain, a mother in shock that the house has been flooded by an overflowing washing machine, someone taking an emergency call with text saying that we are there to take your call 24/7 365 days a year

Target Market(s)

insurance companies and home owners

Industry/Entity Type

Hire

Coding

Coded - Design and coding required

Number of Pages Required

5+ page

Requirements
Must have
• 24/7 emergency contact number on home page (0498215763)
• 4 photos on banner on home page
• Equipment Hire Page should include images and brief description of these 3 products
• http://www.ptkdirect.example.com.au/prod458.htm
• http://www.gustline-gear.example.com.au/product/mistral-breeze-fan/
• http://www.vendrasuck.example.com.au/carpet/carpet-extractor-harrier-xv-x-vi-x-vii
• SERVICES OFFERED ARE:
• 24/7 Emergnecy Flood Restoration
• Insurance Claims
• Structural Drying
• Sub Floor Drying
• Supply and installation of drying equipment
• Professional Carpet and underlay installation
Nice to have
• Some other websites we like
• www.kelbyleakfixers.example.com.au
• www.summitrecoverywashing.example.com.au/flood-water-damage-restoration
• http://www.pelhamrecovery.example.com.au/
• http://www.dampfixnational.example.com.au/
Should not have
• not looking for an all white background.

```html
<!DOCTYPE html>
<html lang="en">
<head>
<meta charset="utf-8">
<title>Brindlecove Flood Restoration</title>
<link href="https://fonts.googleapis.com/css2?family=Open+Sans:wght@400;600;700;800&display=swap" rel="stylesheet">
<style>
:root{
  --blue:#1a8fcf;
  --green:#19b36b;
  --navy:#252d3f;
  --ink:#333;
  --muted:#777;
  --light:#f2f2f2;
  --footer:#333;
  --orange:#ff6a00;
  --amber:#ffb400;
  --yellow:#ffe600;
  --white:#fff;
}
*{margin:0;padding:0;box-sizing:border-box}
html,body{width:686px;height:1200px;overflow:hidden}
body{font-family:'Open Sans',sans-serif;color:var(--ink);position:relative;background:var(--white)}
.abs{position:absolute}

.hero{left:0;top:0;width:686px;height:350px;background:linear-gradient(120deg,#1c6fc4 0%,#1c9bbf 40%,#20b58f 70%,#18b656 100%)}
.header{left:76px;top:5px;width:534px;height:45px;background:var(--white)}
.brand{position:absolute;left:10px;top:0;height:45px;display:flex;align-items:center;gap:6px;width:185px}
.brand-mark{width:16px;height:16px;background:var(--blue);flex:none}
.brand-name{font-size:9.5px;font-weight:700;color:var(--blue);line-height:1.1;white-space:nowrap}
.nav{position:absolute;left:203px;top:0;height:45px;display:flex;align-items:center;gap:14px;font-size:7px;color:var(--ink);white-space:nowrap}
.nav .active{color:var(--blue)}
.emergency{left:423px;top:0;width:111px;height:45px;background:var(--light);padding:11px 0 0 10px}
.emergency small{display:block;font-size:6px;color:var(--ink)}
.emergency strong{display:block;font-size:10px;font-weight:600;color:#111}
.phone-btn{left:84px;top:13px;width:19px;height:19px;border-radius:50%;background:#111;display:flex;align-items:center;justify-content:center}
.hero-copy{left:0;top:142px;width:686px;text-align:center;color:var(--white);font-size:19px;line-height:29px}
.btn-dark{left:311px;top:238px;width:64px;height:22px;background:var(--navy);color:var(--white);font-size:7px;font-weight:700;display:flex;align-items:center;justify-content:center;border-radius:2px}
.dots{left:318px;top:332px;display:flex;gap:9px}
.dots span{width:5px;height:5px;border-radius:50%;border:1px solid var(--white)}
.dots span:not(:first-child){background:var(--white)}

.help{left:0;top:350px;width:686px;height:176px;background:var(--navy)}
.help h2{position:absolute;top:22px;width:686px;text-align:center;color:var(--white);font-size:22px;font-weight:700}
.field{width:115px;height:23px;background:var(--white);border-radius:2px;font-size:6.5px;color:var(--ink);padding:7px 10px}
.btn-grad{left:311px;top:128px;width:64px;height:22px;background:linear-gradient(90deg,var(--blue),var(--green));color:var(--white);font-size:7px;font-weight:700;display:flex;align-items:center;justify-content:center;border-radius:2px}

.welcome{left:0;top:526px;width:686px;height:148px;background:var(--white);text-align:center}
.welcome h2{margin-top:26px;font-size:24px;font-weight:800;color:var(--blue);line-height:28px}
.welcome h3{font-size:9px;font-weight:400;color:var(--ink);line-height:12px}
.welcome p{width:530px;margin:6px auto 0;font-size:6.3px;line-height:12px;color:var(--ink)}

.features{left:0;top:674px;width:686px;height:123px;background:var(--light)}
.feature{top:25px;width:170px}
.feature-icon{width:40px;height:40px;background:linear-gradient(135deg,#0f7d9a,#14a58a);display:flex;align-items:center;justify-content:center}
.feature h4{position:absolute;left:47px;top:2px;font-size:15px;font-weight:700;line-height:18px;color:var(--navy);white-space:nowrap}
.feature p{margin-top:8px;font-size:5.3px;line-height:8px;color:var(--muted)}

.testimonials{left:0;top:797px;width:343px;height:151px;background:linear-gradient(90deg,var(--orange),var(--amber))}
.testimonials h2{position:absolute;left:76px;top:13px;font-size:32px;font-weight:800;color:var(--yellow)}
.quote-mark{left:77px;top:63px}
.testimonials p{position:absolute;left:122px;top:64px;width:200px;font-size:8.4px;line-height:12.8px;color:var(--white)}
.testimonials cite{position:absolute;left:122px;top:116px;font-size:7.5px;font-weight:700;font-style:normal;color:var(--white)}
.photo{left:343px;top:797px;width:343px;height:151px;background:linear-gradient(180deg,#6c7d86 0%,#9aa4a6 55%,#4fb6b7 100%)}
.map{left:0;top:948px;width:686px;height:170px;background:linear-gradient(90deg,#7fc8f0 0%,#56d4d6 50%,#3ee08e 100%)}

.footer{left:0;top:1118px;width:686px;height:82px;background:var(--footer);color:#ddd}
.contact-row{position:absolute;top:12px;left:76px;width:534px;display:flex;align-items:center;font-size:6.4px;white-space:nowrap}
.contact-row .item{display:flex;align-items:center;gap:6px}
.social{display:flex;gap:9px;margin-left:auto}
.social span{width:6px;height:6px;border-radius:50%;background:#ccc}
.footer hr{position:absolute;top:34px;left:76px;width:534px;border:0;border-top:1px solid #4a4a4a}
.footer-links{position:absolute;top:46px;width:686px;text-align:center;font-size:5.3px}
.copyright{position:absolute;top:60px;width:686px;text-align:center;font-size:5.3px}
</style>
</head>
<body>

<section class="hero abs" role="img" aria-label="Flooded house interior with water covering the floor at the foot of a staircase">
</section>

<header class="header abs">
  <div class="brand"><span class="brand-mark"></span><span class="brand-name">Brindlecove Flood Restoration</span></div>
  <nav class="nav">
    <span class="active">Home</span><span>Services</span><span>Gallery</span><span>Equipment hire</span><span>Contact us</span>
  </nav>
  <div class="emergency abs">
    <small>24/7 Emergency Contact</small>
    <strong>0498215763</strong>
    <div class="phone-btn abs">
      <svg width="9" height="9" viewBox="0 0 24 24"><path fill="#fff" d="M6.6 10.8a15 15 0 0 0 6.6 6.6l2.2-2.2c.3-.3.7-.4 1-.2 1.1.4 2.3.6 3.6.6.6 0 1 .4 1 1V20c0 .6-.4 1-1 1A17 17 0 0 1 3 4c0-.6.4-1 1-1h3.5c.6 0 1 .4 1 1 0 1.3.2 2.5.6 3.6.1.3 0 .7-.2 1z"/></svg>
    </div>
  </div>
</header>

<div class="hero-copy abs">Wet Carpets??<br>Washing machine just overflowed??<br>Burst pipe?</div>
<div class="btn-dark abs">CONTACT US</div>
<div class="dots abs"><span></span><span></span><span></span><span></span></div>

<section class="help abs">
  <h2>WE'RE HERE TO HELP!!</h2>
  <div class="field abs" style="left:166px;top:61px">Name</div>
  <div class="field abs" style="left:285px;top:61px">Email</div>
  <div class="field abs" style="left:404px;top:61px">Phone</div>
  <div class="field abs" style="left:166px;top:89px">Address</div>
  <div class="field abs" style="left:285px;top:89px">Service For
    <svg class="abs" style="right:8px;top:9px" width="5" height="4" viewBox="0 0 10 6"><path d="M1 1l4 4 4-4" stroke="#333" fill="none" stroke-width="1.5"/></svg>
  </div>
  <div class="field abs" style="left:404px;top:89px">Message</div>
  <div class="btn-grad abs">CONTACT US</div>
</section>

<section class="welcome abs">
  <h2>WELCOME TO</h2>
  <h3>Brindlecove Flood Restoration</h3>
  <p>Aenean sed quam non sapien faucibus consequat vitae sit amet orci. Praesent quis risus mi. In mollis nulla in pulvinar dictum. Vivamus interdum sagittis felis, ut dapibus ligula feugiat ac. In dictum sapien eu tellus finibus fermentum. Aenean faucibus lacus ut mollis commodo. Donec vestibulum odio sem, ac laoreet massa ullamcorper id. Donec molestie nisi et tellus hendrerit vehicula. Nunc eu ligula sed quam pulvinar maximus in vitae eros. Proin porta fermentum ipsum, vel porttitor turpis venenatis luctus. Vivamus volutpat eu sapien quis tempus. Aenean feugiat viverra lorem ac sagittis. Donec sit amet lectus nec mi tempor laoreet ac nec nunc.</p>
</section>

<section class="features abs">
  <div class="feature abs" style="left:76px">
    <div class="feature-icon"><svg width="20" height="20" viewBox="0 0 24 24"><circle cx="12" cy="12" r="9" stroke="#fff" stroke-width="2.2" fill="none"/><path d="M12 7v5h4" stroke="#fff" stroke-width="2.2" fill="none"/></svg></div>
    <h4>QUICK<br>ARRIVAL</h4>
    <p>Nam et tortor in ante iaculis porttitor in luctus mi. Vivamus gravida sem a pretium euismod. Nam lobortis, purus et fringil la tempus, risus eros dignissim diam.</p>
  </div>
  <div class="feature abs" style="left:263px">
    <div class="feature-icon"><svg width="22" height="18" viewBox="0 0 24 20"><circle cx="12" cy="6" r="3.5" fill="#fff"/><circle cx="5" cy="8" r="2.5" fill="#fff"/><circle cx="19" cy="8" r="2.5" fill="#fff"/><rect x="7" y="11" width="10" height="7" rx="3" fill="#fff"/><rect x="1" y="12" width="7" height="5" rx="2.5" fill="#fff"/><rect x="16" y="12" width="7" height="5" rx="2.5" fill="#fff"/></svg></div>
    <h4>EXPERIENCED<br>TEAM</h4>
    <p>Nam et tortor in ante iaculis porttitor in luctus mi. Vivamus gravida sem a pretium euismod. Nam lobortis, purus et fringil la tempus, risus eros dignissim diam.</p>
  </div>
  <div class="feature abs" style="left:450px">
    <div class="feature-icon"><svg width="22" height="22" viewBox="0 0 24 24"><circle cx="9" cy="13" r="6" stroke="#fff" stroke-width="3" stroke-dasharray="3 2" fill="none"/><circle cx="9" cy="13" r="2" fill="#fff"/><circle cx="18" cy="6" r="3.5" stroke="#fff" stroke-width="2" stroke-dasharray="2 1.5" fill="none"/></svg></div>
    <h4>ADVANCED<br>TECHNOLOGY</h4>
    <p>Nam et tortor in ante iaculis porttitor in luctus mi. Vivamus gravida sem a pretium euismod. Nam lobortis, purus et fringil la tempus, risus eros dignissim diam.</p>
  </div>
</section>

<section class="testimonials abs">
  <h2>TESTIMONIALS</h2>
  <svg class="quote-mark abs" width="30" height="26" viewBox="0 0 30 26"><path d="M0 26V14C0 6 4 1 12 0v5c-4 1-6 4-6 8h6v13zM17 26V14c0-8 4-13 12-14v5c-4 1-6 4-6 8h6v13z" fill="#ffffff" opacity=".55"/></svg>
  <p>Pellentesque blandit lacus eget nunc faucibus, et tincidunt eros viverra. Phasellus consequat sagittis nisi suscipit feugiat. Cras eget leo sed nunc hendre-rit ultricies eu at nisl consequat.</p>
  <cite>~ MARA QUINLAN, CITY</cite>
</section>
<div class="photo abs" role="img" aria-label="Laundry room flooded by an overflowing washing machine, a woman at an ironing board seen from behind"></div>

<section class="map abs" role="img" aria-label="World map tinted in blue and green showing service coverage"></section>

<footer class="footer abs">
  <div class="contact-row">
    <div class="item" style="width:182px"><svg width="6" height="8" viewBox="0 0 12 16"><path d="M6 0a6 6 0 0 0-6 6c0 4.5 6 10 6 10s6-5.5 6-10a6 6 0 0 0-6-6zm0 8.5A2.5 2.5 0 1 1 6 3.5a2.5 2.5 0 0 1 0 5z" fill="#ddd"/></svg>18 Harbour Lane, Brindlecove, City - 0000</div>
    <div class="item" style="width:124px"><svg width="7" height="7" viewBox="0 0 24 24"><path fill="#ddd" d="M6.6 10.8a15 15 0 0 0 6.6 6.6l2.2-2.2c.3-.3.7-.4 1-.2 1.1.4 2.3.6 3.6.6.6 0 1 .4 1 1V20c0 .6-.4 1-1 1A17 17 0 0 1 3 4c0-.6.4-1 1-1h3.5c.6 0 1 .4 1 1 0 1.3.2 2.5.6 3.6.1.3 0 .7-.2 1z"/></svg>Call Now : 555 014 7720</div>
    <div class="item"><svg width="9" height="7" viewBox="0 0 18 13"><rect width="18" height="13" rx="1" fill="#ddd"/><path d="M1 1l8 6 8-6" stroke="#333" stroke-width="1.4" fill="none"/></svg>Email: info@brindlecoveflood.example.com</div>
    <div class="social"><span></span><span></span><span></span><span></span></div>
  </div>
  <hr>
  <div class="footer-links">Home &nbsp;|&nbsp; Services &nbsp;|&nbsp; Gallery &nbsp;|&nbsp; Equipment hire &nbsp;|&nbsp; Contact us</div>
  <div class="copyright">Copyright © 2016 Brindlecove Flood Restoration. &nbsp;All rights reserved.</div>
</footer>

</body>
</html>
```